Bright Oak Fitness Facility Business Cards

Business Card Design that incorporates the logo and tagline

Target Market(s)

Fitness, People Who Exercise

Contact Information for Business Card

2718 Harrow Creek Bend
Millbrook Falls, Oregon 97999
Phone: 555-010-Team (8326)
www.brightoakfitness.example
info@brightoakfitness.example

Requirements
Must have
• Logo, Address, Website, email and tagline "Built For Every Body". Colors should be red/black/grey/white

```html
<!DOCTYPE html>
<html lang="en">
<head>
<meta charset="utf-8">
<title>Bright Oak Fitness Facility – Business Cards</title>
<link rel="stylesheet" href="https://fonts.googleapis.com/css2?family=Open+Sans:wght@400;600;700&display=swap">
<style>
  :root {
    --brand-red: #ed1c24;
    --ink: #1f1f1f;
    --grey-text: #3a3a3a;
    --rule-grey: #8a8a8a;
    --paper: #ffffff;
    --backdrop: #e4e1dd;
  }
  * { margin: 0; padding: 0; box-sizing: border-box; }
  html, body {
    width: 1200px; height: 997px; overflow: hidden;
    background: var(--backdrop);
    font-family: "Open Sans", Arial, sans-serif;
  }
  .canvas { position: relative; width: 1200px; height: 997px; }

  .card {
    position: absolute; left: 270px;
    width: 660px; height: 377px;
    box-shadow: 0 6px 18px rgba(0,0,0,0.12);
    overflow: hidden;
  }
  .card--front { top: 90px; background: var(--paper); }
  .card--back { top: 520px; background: var(--brand-red); color: var(--paper); }

  /* front side */
  .edge-band {
    position: absolute; top: 0; right: 0; width: 14px; height: 100%;
    background: var(--brand-red);
  }
  .edge-band__tab {
    position: absolute; top: 70px; right: 14px; width: 26px; height: 40px;
    background: var(--ink);
  }
  .front-logo {
    position: absolute; left: 48px; top: 62px;
    display: flex; align-items: center; gap: 12px;
  }
  .logo-square { width: 26px; height: 26px; background: var(--brand-red); flex: none; }
  .logo-name {
    font-weight: 700; font-size: 30px; letter-spacing: 0.5px;
    text-transform: uppercase; color: var(--ink); line-height: 1;
    white-space: nowrap;
  }
  .holder {
    position: absolute; right: 62px; top: 60px; text-align: right;
  }
  .holder__name { color: var(--brand-red); font-weight: 700; font-size: 17px; }
  .holder__role { color: var(--grey-text); font-size: 14px; margin-top: 2px; }
  .front-rule {
    position: absolute; left: 48px; right: 40px; top: 124px;
    height: 1px; background: var(--rule-grey);
  }
  .contact {
    position: absolute; left: 48px; top: 226px;
    border-top: 1px solid var(--rule-grey); padding-top: 12px;
    list-style: none; font-size: 15px; color: var(--grey-text);
  }
  .contact li { display: flex; align-items: center; gap: 8px; line-height: 24px; white-space: nowrap; }
  .contact svg { width: 13px; height: 13px; fill: var(--brand-red); flex: none; }
  .contact .address { margin-top: 6px; }

  /* back side */
  .back-logo {
    position: absolute; left: 0; right: 0; top: 120px;
    display: flex; justify-content: center; align-items: center; gap: 14px;
  }
  .logo-square--light { background: var(--paper); }
  .logo-name--light { color: var(--paper); font-size: 34px; }
  .back-underline {
    position: absolute; left: 230px; width: 200px; top: 180px;
    height: 2px; background: var(--paper);
  }
  .tagline {
    position: absolute; left: 0; right: 0; top: 246px;
    display: flex; justify-content: center; align-items: center; gap: 14px;
    font-size: 15px; letter-spacing: 1px; white-space: nowrap;
  }
  .tagline::before, .tagline::after {
    content: ""; width: 34px; height: 1px; background: var(--paper);
  }
</style>
</head>
<body>
<main class="canvas">
  <section class="card card--front" aria-label="Business card front">
    <div class="edge-band"></div>
    <div class="edge-band__tab"></div>

    <div class="front-logo">
      <span class="logo-square"></span>
      <span class="logo-name">Bright Oak Fitness</span>
    </div>

    <div class="holder">
      <p class="holder__name">Dana Pruitt</p>
      <p class="holder__role">President</p>
    </div>
    <div class="front-rule"></div>

    <ul class="contact">
      <li>
        <svg viewBox="0 0 24 24" aria-hidden="true"><path d="M6.6 10.8a15.1 15.1 0 0 0 6.6 6.6l2.2-2.2a1 1 0 0 1 1-.25 11.4 11.4 0 0 0 3.6.57 1 1 0 0 1 1 1V20a1 1 0 0 1-1 1A17 17 0 0 1 3 4a1 1 0 0 1 1-1h3.5a1 1 0 0 1 1 1c0 1.25.2 2.45.57 3.6a1 1 0 0 1-.25 1z"/></svg>
        555-010-Team (8326)
      </li>
      <li>
        <svg viewBox="0 0 24 24" aria-hidden="true"><path d="M2 5h20v14H2zm2 2v.5l8 5 8-5V7l-8 5z"/></svg>
        info@brightoakfitness.example
      </li>
      <li>
        <svg viewBox="0 0 24 24" aria-hidden="true"><path d="M12 2a10 10 0 1 0 0 20 10 10 0 0 0 0-20zm0 2c.9 1.2 1.6 2.6 2 4h-4c.4-1.4 1.1-2.8 2-4zM4.3 14a8 8 0 0 1 0-4h3.4a16 16 0 0 0 0 4zm.8 2h3a15 15 0 0 0 1.4 3.6A8 8 0 0 1 5.1 16zM8.1 8h-3a8 8 0 0 1 4.4-3.6A15 15 0 0 0 8.1 8zM12 20c-.9-1.2-1.6-2.6-2-4h4c-.4 1.4-1.1 2.8-2 4zm2.3-6H9.7a14 14 0 0 1 0-4h4.6a14 14 0 0 1 0 4zm.2 5.6A15 15 0 0 0 15.9 16h3a8 8 0 0 1-4.4 3.6zM16.3 14a16 16 0 0 0 0-4h3.4a8 8 0 0 1 0 4z"/></svg>
        www.brightoakfitness.example
      </li>
      <li class="address">2718 Harrow Creek Bend Millbrook Falls, Oregon 97999</li>
    </ul>
  </section>

  <section class="card card--back" aria-label="Business card back">
    <div class="back-logo">
      <span class="logo-square logo-square--light"></span>
      <span class="logo-name logo-name--light">Bright Oak Fitness</span>
    </div>
    <div class="back-underline"></div>
    <p class="tagline">Built For Every Body</p>
  </section>
</main>
</body>
</html>
```